Flyer-Design für Wechseljahres Tag Seminar Vol. 2
Zielgruppe
Seminare, Vorträge , Therapien, Beratung, Coaching
WEchseljahre Beratung
Sexualtherapie, Sexualberatung
Mentaltraining
Es soll Frauen gefallen und ermuntern zum Seminar zu kommen, frü Thema Wechseljahre interessieren
Aufgabenstellung
Grösse A5 Hochkant

```html
<!DOCTYPE html>
<html lang="de">
<head>
<meta charset="utf-8">
<title>Wechseljahre Seminar</title>
<link href="https://fonts.googleapis.com/css2?family=Oswald:wght@300;400;500&family=Source+Sans+3:wght@400;600;700&family=Roboto+Slab:wght@700;800&display=swap" rel="stylesheet">
<style>
:root{
  --blue:#1aa6d4;
  --yellow:#f4ea3d;
  --green:#c6c63e;
  --ink:#2b2b1f;
  --white:#ffffff;
}
*{margin:0;padding:0;box-sizing:border-box}
html,body{width:865px;height:1200px;overflow:hidden;background:#fff}
.flyer{position:relative;width:865px;height:1200px;overflow:hidden;background:var(--green);font-family:"Source Sans 3",sans-serif;color:var(--ink)}
.hero-photo{position:absolute;left:0;top:0;width:865px;height:560px;
  background:linear-gradient(180deg,#e9efd6 0%,#cfdca0 35%,#b9c768 70%,var(--green) 100%)}
.shapes{position:absolute;left:0;top:0}
.date{position:absolute;left:19px;top:40px;font-family:"Oswald",sans-serif;line-height:1}
.date .day{font-size:74px;font-weight:500;color:var(--yellow);letter-spacing:-1px}
.date .year{font-size:52px;font-weight:400;color:var(--white)}
.date .label{display:block;font-size:56px;font-weight:300;color:var(--yellow);margin:10px 0 0 50px}
.info{position:absolute;left:525px;top:14px;width:330px;text-align:center;font-family:"Oswald",sans-serif;color:var(--white);line-height:1.2}
.info .time{font-size:27px;font-weight:400}
.info .time b{font-size:38px;font-weight:500;color:var(--yellow)}
.info .place{font-size:25px;font-weight:400;margin-top:2px}
.info .place span{font-weight:300}
.headline{position:absolute;left:95px;top:452px;font-size:28px;font-weight:700;color:var(--blue);line-height:32px}
.intro{position:absolute;left:95px;top:556px;width:676px;columns:2;column-gap:16px;font-size:10.6px;line-height:15.6px;color:#2c2c24}
.section-title{position:absolute;left:95px;font-size:29px;font-weight:700;color:var(--white)}
.list{position:absolute;list-style:none;font-size:11.6px;font-weight:700;line-height:16px;color:#23231b}
.list li{position:relative;padding-left:15px;margin-bottom:4px}
.list li::before{content:"";position:absolute;left:0;top:3px;width:9px;height:9px;background:var(--white)}
.band{position:absolute;left:0;top:936px;width:865px;height:143px;background:var(--blue)}
.band-text{position:absolute;left:52px;top:18px;width:480px;font-family:"Roboto Slab",serif;font-weight:700;font-size:14.6px;line-height:22px;color:var(--white)}
.price{position:absolute;left:548px;top:6px;font-family:"Oswald",sans-serif;color:var(--yellow);font-weight:500;white-space:nowrap}
.price .cur{font-size:30px}
.price .amount{font-size:72px;line-height:1}
.price sup{font-size:30px;vertical-align:34px}
.price-note{position:absolute;left:545px;top:74px;width:240px;text-align:center;font-size:12px;font-style:italic;line-height:18px;color:#123}
.footer{position:absolute;left:0;top:1079px;width:865px;height:121px;background:var(--white)}
.register{position:absolute;left:0;top:14px;width:865px;text-align:center}
.register h2{font-family:"Roboto Slab",serif;font-weight:800;font-size:22px;color:var(--blue);margin-bottom:2px}
.register p{font-size:13.6px;line-height:20px;color:#333}
.register .link{color:var(--blue);font-weight:700}
.portrait{position:absolute;left:48px;top:1053px;width:104px;height:104px;border-radius:50%;border:4px solid var(--white);
  background:radial-gradient(circle at 50% 45%,#e8cfc2 0%,#c9a79a 45%,#9aa7c0 100%)}
.brand{position:absolute;left:711px;top:1054px;width:110px;height:110px;border-radius:50%;background:#5ab8d6;border:4px solid var(--white);
  display:flex;align-items:center;justify-content:center;font-size:13px;font-weight:700;color:var(--white)}
.bottom-bar{position:absolute;left:360px;top:1196px;width:147px;height:4px;background:var(--blue)}
</style>
</head>
<body>
<div class="flyer">
  <div class="hero-photo" role="img" aria-label="Foto: Frau mittleren Alters sitzt entspannt auf einer sonnigen Frühlingswiese"></div>
  <svg class="shapes" width="865" height="240" viewBox="0 0 865 240" aria-hidden="true">
    <ellipse cx="150" cy="40" rx="190" ry="206" fill="var(--blue)" stroke="#fff" stroke-width="5"/>
    <ellipse cx="710" cy="-40" rx="240" ry="190" fill="var(--blue)" stroke="#fff" stroke-width="5"/>
  </svg>

  <div class="date">
    <span class="day">23.09.</span><span class="year">2017</span>
    <span class="label">SEMINAR</span>
  </div>
  <div class="info">
    <div class="time">VON <b>9.00 – 15.00</b> UHR</div>
    <div class="place"><span>ORT:</span> BILDUNGSHAUS TALWIESE,<br>3920 ALMSDORF</div>
  </div>

  <h1 class="headline">Ein Neuwerden, ein Loslassen,<br>ein einzigartiges Geschenk und<br>Herausforderung zugleich!</h1>
  <p class="intro">Viele Frauen befinden, dass mit dem Klimakterium eine Last von ihren Schultern fällt. Endlich dürfen sie sich fallen lassen, endlich an sich selbst denken. Für solche Frauen beginnt mit den hormonellen Wallungen eine Phase des Perspektivwechsels. Die Zeit des Klimakteriums lädt zu einer inneren Inventur und gegebenenfalls einer Neuorientierung ein. Statt von einem Gefühlschaos überwältigt zu werden, empfinden sich viele Frauen als emotionell empfindsamer, zugänglicher und berührbarer. Moderatorin und Sängerin Mira Sonntag nimmt’s mit Humor. Sie nennt die Wechseljahre ihren „inneren Sommer“ und träumt von einer implantierten Klimaanlage.</p>

  <h2 class="section-title" style="top:646px">Wenn Sie erfahren möchten,</h2>
  <ul class="list" style="left:127px;top:688px;width:330px">
    <li>wie sich Ihr Körper in den Wechseljahren verändert,</li>
    <li>welche Beschwerden dadurch<br>verursacht werden können</li>
  </ul>
  <ul class="list" style="left:482px;top:688px;width:300px">
    <li>was Sie aktiv zur Linderung und<br>Vorbeugung beitragen können,</li>
    <li>wie Sie Ihre eigene Balance und Heilung finden</li>
  </ul>

  <h2 class="section-title" style="top:754px">Wollen Sie wissen:</h2>
  <ul class="list" style="left:127px;top:796px;width:300px">
    <li>Was mit Ihnen passiert und wie Sie diese<br>neue Lebensphase auf natürliche Weise<br>bewältigen und annehmen können</li>
    <li>Worum es wirklich geht in diesen Jahren</li>
    <li>Wie Sie mutig und lustvoll durch<br>die Wechseljahre kommen</li>
  </ul>
  <ul class="list" style="left:482px;top:796px;width:320px">
    <li>Mehr wissen über Östrogene,<br>Progesterone und Testosterone</li>
    <li>Dieser Tag macht Mut zum Aufbruch und Neugier<br>auf diese neue Lebensphase. Sie erleben,<br>wie es sein wird, Altes loszulassen, den Blick<br>nach vorn zu richten und wichtige Weichen<br>für Ihren weiteren Lebensweg zu stellen.</li>
  </ul>

  <section class="band">
    <p class="band-text">Dieser Tag macht Mut zum Aufbruch und Neugier auf diese neue Lebensphase. Sie erleben, wie es sein wird, Altes loszulassen, den Blick nach vorn zu richten und wichtige Weichen für Ihren weiteren Lebensweg zu stellen.</p>
    <div class="price"><span class="cur">CHF </span><span class="amount">139.</span><sup>00</sup></div>
    <p class="price-note">Kosten Seminar inkl. Getränke, Obst,<br>Z’Nüni und 4 Gang Mittags Menu</p>
  </section>

  <footer class="footer">
    <div class="register">
      <h2>Anmeldung unter:</h2>
      <p class="link">www.lebenswende-tag.ch / info@lebensfreude-raum.ch / 079 / 41 26 803</p>
      <p><span class="link">Lena Brunnhofer</span>, Dipl. Wechseljahresberaterin, Sexualtherapeutin und Mentaltrainerin</p>
      <p class="link">www.Lebensfreude-raum.ch</p>
    </div>
  </footer>
  <div class="portrait" role="img" aria-label="Porträtfoto der Seminarleiterin"></div>
  <div class="brand">Lebensfreude</div>
  <div class="bottom-bar"></div>
</div>
</body>
</html>
```